Major Australian Food and Wine Event Web Design Project

The project will consist of 3 designs
The homepage
A city hub page
A general content page

The main audience who will visit the website will be (in Order of importance:

1) Visitors
- Mainly women 24 – 54 years (they are the main ticket buyers)
- In a relationship – so will go to the show with their partner
- In a good paying job or home maker – and who have disposable income to spend $30 a ticker
- Enjoy food, wine and going out
- Looking for a fun day out – although an event that is about food and wine – it is an event that most people will go to and have a fun day out – not too pretentious

A smaller proportion of the audience will be:
2) Exhibitors & sponsors ( both prospective and existing)
3) Media

Objectives:

- Functionality on home page and sub pages needs to be updated, clear, easy to navigate and inject a sense of ‘fun’ – need to make it look more professional
- Need to incorporate the many things that need to be on the home page and sub pages in a visually appealing manner
- Ensure the ‘Cons’ above are considered and reflected in functionality and design
- To not be too focus on the colours (these can be changed) – but focus on the functionality and overall design opportunities.

Approach:

Keywords to describe the Bright Plate & Vine Fair:
Fun day out, discover, learn, indulge, entertaining

Other website examples:

Some great consumers event websites from the UK really make our website look basic and juvenile – and below are some examples of the presentation of how we would like our website to look like:

http://www.morselfairs-example.com/london/ This website is clean, includes good social media integration and exudes a sense of fun. Their content pages, such as the features landing page also presents options in a clear and visually appealing way with a series of boxes including image and text http://www.morselfairs-example.com/london/content/343/Features

http://www.homecraftexpo-example.com/ - this is also a great website – and it incorporates all the elements we would be looking for on our homepage – but the background/skin also includes a sense of fun and cheekiness. Subpages also are consistent.

Features

• Its a fun day that offers great value for money
• Caters to all visitors, regardless of different levels of knowledge or interest in food, wine and cooking.
• Sample great quality food and wine products from hundreds of reputable exhibitors
• Learn more through many of the shows feature activities (Celeb Theatre, Wine Theatre, Cooking & Cheese Classes)

Functionality & Structure:

In a user friendly, easy to view way, we need to incorporate the following functionality elements on home page:
- main header (that will incorporate our current creative) with a ‘fun’ skin
- navigation tabs/references (hone, location, tickets, blog, sign up, exhibitors)
- navigation/content banner (rotating)
- Area for small intro about the show
- News and highlight section
- New exhibitors section
- Obvious Ticket call to action
- Obvious sign up call to action
- Social media buttons or links ( really like the moving gifs on the Homecraftexpo-example.com site
- area for advertising (MREC size) to sell to exhibitors/sponsors
- Show dates for all 5 shows (maybe in main header)

Subpage layout is also important and needs to reflect the homepage – so would also like to see examples of how this would look and tie in with navigation – we generally have a lot of content on these pages, so clear navigation would be useful. – see below for further details of functionality for city Hubs

‘CITY HUB’ BRIEF
When navigating to each location the user will be taken to a ‘CITY HUB’ which should replicate design and content elements of a main HOME page, as well as reflect more specific information for each Show. Elements which must appear on this page are:
• FEATURES – which may be displayed in categories (in boxes, see appendix 1.0) which will link through to relevant content pages. Or in one box which will link through to a features page with all presented in boxes
• CHEFS – may be displayed as a separate icon box which will link to chefs page with bios, Celeb Theatre timetable etc.
• TICKETS – either a button or clear callout to purchase tickets
• PLAN YOUR DAY – may be displayed in a separate content box which will then link through to getting there, sample itineraries and downloadable pocket show guide for visitors to print before coming to the Show.
• WHO’S EXHIBITING – to link back to city specific exhibitor lists

Our current website is out of date and has the following inadequacies (www.brightplatefair-example.com.au) -

The homepage
A city hub page
A general content page

1) Visitors

3) Media

Objectives:

Approach:

To be perceived as a fun, entertaining event with something for everyone - website creative and navigation must reflect this.

Other website examples:

Features

- New exhibitors section

‘CITY HUB’ BRIEF

- Dated design/layout
- Homepage too text heavy
- No content boxes that can be used for different features/areas (eg. News, Exhibitors etc)
- Uninspiring colours and skin(eg. grey background), does not reflect ‘a fun day out’
- Limited presence of social media platforms and lacks ‘community’
- No continuity in sub pages
- main banner too big – takes up too much space on homepage

Requirements
Must have
• As per above brief.

In addition:
Floating social media buttons on side
Wrap around image
Drop down menu (specifically for the location nav item)

```html
<!DOCTYPE html>
<html lang="en">
<head>
<meta charset="utf-8">
<title>Bright Plate &amp; Vine Fair</title>
<link href="https://fonts.googleapis.com/css2?family=Ubuntu:wght@300;400;500;700&family=Kaushan+Script&family=Open+Sans:wght@400;600;700&display=swap" rel="stylesheet">
<style>
:root{
  --green:#8cba0c;
  --green-dark:#5f8f08;
  --green-light:#a8d11a;
  --orange:#f04a1c;
  --red:#e8401a;
  --red-dark:#c02a0c;
  --text:#444;
  --muted:#777;
  --white:#fff;
  --line:#dcdcdc;
}
*{box-sizing:border-box;margin:0;padding:0}
html,body{width:920px;height:1200px;overflow:hidden}
body{position:relative;font-family:Arial,Helvetica,sans-serif;color:var(--text);
  background:radial-gradient(ellipse at 10% 30%,#b9d57a 0%,transparent 45%),radial-gradient(ellipse at 95% 70%,#cfe49a 0%,transparent 40%),radial-gradient(ellipse at 5% 85%,#a7c95b 0%,transparent 40%),linear-gradient(#f2f5ea,#e6eedb)}
.abs{position:absolute}
.page{position:absolute;left:62px;top:10px;width:796px;height:1148px;background:var(--white);border-radius:22px;box-shadow:0 0 18px rgba(0,0,0,.15)}
.brand{left:92px;top:24px;width:130px;font-family:Ubuntu,sans-serif;font-weight:700;font-size:22px;line-height:24px;color:#2b2b2b}
.promo{left:255px;top:22px;width:361px;height:55px;border:1px solid #eee;background:linear-gradient(90deg,#fbeee6,#fff 40%,#fff 60%,#f5f5ee)}
.promo .ph{position:absolute;top:0;height:53px}
.promo .ph.a{left:0;width:70px;background:linear-gradient(#f3dccb,#e2c6b0)}
.promo .ph.b{right:0;width:118px;background:linear-gradient(90deg,#9bc24a,#e0782a,#c93b1d)}
.promo strong{position:absolute;left:95px;top:12px;font:400 16px Ubuntu,sans-serif;color:var(--orange)}
.promo span{position:absolute;left:95px;top:30px;font:400 12px Arial,sans-serif;color:#b5a98f}
.toplinks{right:90px;top:17px;font-size:10px;color:#666}
.toplinks span{padding:0 6px;border-left:1px solid #ccc}
.toplinks span:first-child{border:0}
.cart{left:666px;top:42px;width:176px;height:30px;border-radius:15px;background:linear-gradient(#fff,#efefef);box-shadow:0 1px 3px rgba(0,0,0,.2);font-size:9.5px;color:#555;padding:10px 0 0 44px}
.cart b{color:var(--green)}
.cart svg{position:absolute;left:18px;top:6px}
.tagline{left:300px;top:88px;width:290px;text-align:center;font:300 20px Ubuntu,sans-serif;color:var(--green-light)}
.tagline b{font-weight:500;color:var(--orange)}
.follow{left:623px;top:102px;font:400 15px "Kaushan Script",cursive;color:#555}
.social{left:716px;top:100px;display:flex;gap:4px}
.social span{width:25px;height:25px;border-radius:50%;background:var(--green);color:#fff;font:400 6px Ubuntu,sans-serif;display:flex;align-items:center;justify-content:center;text-align:center}
.social span:nth-child(2){background:#e8672a}.social span:nth-child(3){background:#556fa6}.social span:nth-child(4){background:#c33}
.nav{left:68px;top:130px;width:785px;height:34px;border-radius:17px;background:linear-gradient(#fff,#ececec);box-shadow:0 1px 3px rgba(0,0,0,.18)}
.nav a{position:absolute;top:11px;font:400 12px Ubuntu,sans-serif;color:#555;text-decoration:none;transform:translateX(-50%)}
.nav .sep{position:absolute;top:4px;width:1px;height:27px;background:#ddd}
.home{left:91px;top:126px;width:70px;height:46px;background:linear-gradient(var(--green-light),var(--green-dark));color:#fff;font:400 12px Ubuntu,sans-serif;text-align:center;padding-top:16px;border-radius:2px}
.search{left:690px;top:138px;width:124px;height:20px;border-radius:10px;border:1px solid #ddd;background:#fff}
.searchicon{left:818px;top:140px}
.hero-img{left:75px;top:180px;width:390px;height:290px;background:radial-gradient(ellipse at 50% 55%,#d8e44a 0%,#f0f1c8 40%,#fff 70%)}
.hero-title{left:368px;top:193px;font:700 31px Ubuntu,sans-serif;color:var(--orange);letter-spacing:.5px}
.hero-text{left:368px;top:230px;width:428px;font-size:10px;line-height:19px;color:#666}
.price{left:467px;top:310px;font:300 38px Ubuntu,sans-serif;color:var(--green-light)}
.buy{left:635px;top:358px;width:187px;height:40px;border-radius:8px;background:linear-gradient(var(--green-light),var(--green-dark));border:2px solid #d9ec8c;color:#fff;font:400 18px Ubuntu,sans-serif;padding:8px 0 0 10px}
.buy i{position:absolute;right:10px;top:6px;width:22px;height:24px;background:#f3c72a;transform:rotate(-15deg)}
.arrow{top:282px}
.dots{left:383px;top:456px;width:148px;height:28px;border-radius:14px;background:linear-gradient(#fff,#e8e8e8);box-shadow:0 1px 3px rgba(0,0,0,.2)}
.dots i{position:absolute;top:8px;width:13px;height:13px;border-radius:50%;background:var(--orange)}
.dots i:first-child{background:var(--green)}
.shadow{height:10px;background:radial-gradient(ellipse at 50% 0,rgba(0,0,0,.25),transparent 70%)}
.welcome{left:70px;top:512px;width:781px;height:128px;background:linear-gradient(var(--green-light),var(--green-dark))}
.welcome .photo{position:absolute;left:4px;top:3px;width:175px;height:122px;background:#fff;padding:5px}
.welcome .photo div{width:100%;height:100%;background:linear-gradient(135deg,#6b4a2a,#e9d9c4 45%,#9a3b1c)}
.welcome h2{position:absolute;left:205px;top:10px;font:300 19px Ubuntu,sans-serif;color:#fff}
.welcome h2 b{font-weight:700}
.welcome p{position:absolute;left:205px;top:42px;width:565px;font:400 10px/16px "Open Sans",sans-serif;color:#fff}
.about-h{left:103px;top:664px;font:400 14px Ubuntu,sans-serif;color:#666}
.about-h em{font:400 16px "Kaushan Script",cursive;color:var(--green);font-style:normal}
.about-icon{left:70px;top:656px;width:30px;height:36px;background:linear-gradient(#eee,#ccc);border-radius:4px}
.about-rule{left:103px;top:690px;width:285px;border-top:1px dotted #ccc}
.about{left:76px;top:710px;width:560px;font-size:9.6px;line-height:16px;color:#555}
.about p{margin-bottom:16px}
.more{left:570px;top:859px;width:60px;height:16px;border-radius:8px;background:linear-gradient(var(--green-light),var(--green-dark));color:#fff;font-size:9.5px;text-align:center;padding-top:2px}
.tab{left:665px;width:186px;height:28px;color:#fff;font:500 14px Ubuntu,sans-serif;padding:5px 0 0 10px;clip-path:polygon(0 0,85% 0,100% 100%,0 100%)}
.tab.exhibit{top:661px;background:linear-gradient(var(--orange),var(--red-dark))}
.tab.volunteer{top:707px;background:linear-gradient(var(--green-light),var(--green-dark))}
.signup{left:665px;top:758px;width:185px;height:144px;border-radius:10px;background:linear-gradient(#f45a24,var(--red-dark));color:#fff}
.signup h3{position:absolute;left:17px;top:8px;font:500 16px Ubuntu,sans-serif}
.signup label{position:absolute;font-size:9.5px}
.signup .field{position:absolute;left:69px;width:105px;height:16px;border-radius:8px;background:#fff}
.signup .check{position:absolute;left:75px;top:109px;width:10px;height:10px;background:#fff;border:1px solid #999}
.signup .btn{position:absolute;left:132px;top:111px;width:42px;height:17px;border-radius:5px;background:#f2f2f2;color:#555;font-size:9.5px;text-align:center;padding-top:3px}
.card{top:916px;width:178px;height:222px;border-radius:10px;background:linear-gradient(#fff,#ececec);border:1px solid #e4e4e4}
.card.active{background:linear-gradient(var(--green-light),var(--green-dark));border:0}
.card .img{position:absolute;left:10px;top:10px;width:158px;height:99px;border:3px solid #fff;box-shadow:0 0 2px rgba(0,0,0,.3)}
.card h4{position:absolute;left:9px;top:117px;font:400 14px Ubuntu,sans-serif;color:var(--orange)}
.card h4 b{font-weight:400;color:var(--green)}
.card.active h4,.card.active h4 b{color:#fff}
.card hr{position:absolute;left:9px;top:139px;width:160px;border:0;border-top:1px dotted #bbb}
.card p{position:absolute;left:9px;top:144px;width:160px;font-size:9.4px;line-height:14.5px;letter-spacing:.4px;color:#555}
.card p b{color:#444}
.card.active p,.card.active p b{color:#fff}
.card .plus{position:absolute;right:-2px;bottom:2px;width:32px;height:32px;border-radius:50%;background:#fff}
.card .plus svg{position:absolute;left:7px;top:7px}
.newex{left:659px;top:930px;width:192px;height:208px;border-radius:10px;background:linear-gradient(#fff,#efefef);border:1px solid #e4e4e4}
.newex h4{position:absolute;left:32px;top:8px;font:400 15px Ubuntu,sans-serif;color:#999}
.newex h4 b{font-weight:700}
.newex .item{position:absolute;left:11px;width:172px;height:52px;border-bottom:1px dotted #ccc}
.newex .thumb{position:absolute;left:0;top:4px;width:50px;height:40px;border:2px solid #fff;box-shadow:0 0 2px rgba(0,0,0,.3);background:linear-gradient(135deg,#6b4a2a,#e9d9c4 50%,#9a3b1c)}
.newex .item b{position:absolute;left:59px;top:2px;font:700 10px "Open Sans",sans-serif;color:var(--green-dark)}
.newex .item span{position:absolute;left:59px;top:16px;font-size:8.5px;line-height:14px;color:#555}
.pay{left:78px;top:1170px;display:flex;gap:3px}
.pay span{height:23px;padding:5px 6px 0;border:1px solid #bbb;background:#fff;font:700 10px Arial,sans-serif;color:#333}
.footer{right:54px;font-size:9.8px;color:#333;text-align:right}
.footer span{padding:0 8px}
</style>
</head>
<body>
<div class="page"></div>

<div class="abs brand">Bright Plate &amp; Vine Fair</div>

<div class="abs promo">
  <div class="ph a" role="img" aria-label="Smiling shopper holding groceries"></div>
  <strong>FREE DELIVERY</strong><span>ON ORDERS OVER $9.99</span>
  <div class="ph b" role="img" aria-label="Fresh vegetables"></div>
</div>

<div class="abs toplinks"><span>Login</span><span>Create an Account</span><span>Tools</span></div>
<div class="abs cart">
  <svg width="20" height="18" viewBox="0 0 20 18"><path d="M2 6h16l-2 9H4z" fill="#a8d11a"/><path d="M6 6l3-5M14 6l-3-5" stroke="#5f8f08" stroke-width="1.5" fill="none"/></svg>
  Now in your cart &nbsp;<b>0 items</b>
</div>

<div class="abs tagline">Mainly women <b>24 – 54</b> years</div>
<div class="abs follow">Follow us on</div>
<div class="abs social"><span>Chirp<br>line</span><span>Feed</span><span>Friend<br>wall</span><span>Clip<br>cast</span></div>

<nav class="abs nav">
  <a style="left:158px">location</a><a style="left:254px">tickets</a><a style="left:339px">blog</a><a style="left:430px">sign up</a><a style="left:535px">exhibitors</a>
  <i class="sep" style="left:125px"></i><i class="sep" style="left:211px"></i><i class="sep" style="left:300px"></i><i class="sep" style="left:385px"></i><i class="sep" style="left:476px"></i><i class="sep" style="left:590px"></i>
</nav>
<div class="abs home">Home</div>
<div class="abs search"></div>
<svg class="abs searchicon" width="20" height="18" viewBox="0 0 20 18"><circle cx="7" cy="7" r="5" stroke="#8cba0c" stroke-width="2.5" fill="none"/><path d="M11 10l7 6" stroke="#8cba0c" stroke-width="3"/></svg>

<div class="abs hero-img" role="img" aria-label="Green cocktail with sliced lemons, kiwi fruit and ice"></div>
<div class="abs hero-title">Beef Portabello Dinner</div>
<div class="abs hero-text">Lorem ipsum dolor sit amet, consectetur adipisicing elit, sed do eiusmod tempor incididunt ut labore et dolore magna aliqua. Ut enim adLorem ipsum dolor sit amet, consectetur adipi-sicing elit, sed do eiusmod tempor incididunt ut labore et dLorem ipsum dolor sit amet, consectetur adipisicing elit, sed do eiusmod.</div>
<div class="abs price">$12.89</div>
<div class="abs buy">Purchase Tickets<i></i></div>
<svg class="abs arrow" style="left:64px" width="26" height="34" viewBox="0 0 26 34"><path d="M22 2L6 17l16 15" stroke="#ccc" stroke-width="6" fill="none"/></svg>
<svg class="abs arrow" style="left:828px" width="26" height="34" viewBox="0 0 26 34"><path d="M4 2l16 15L4 32" stroke="#ccc" stroke-width="6" fill="none"/></svg>
<div class="abs dots"><i style="left:21px"></i><i style="left:45px"></i><i style="left:69px"></i><i style="left:93px"></i><i style="left:117px"></i></div>
<div class="abs shadow" style="left:72px;top:472px;width:780px"></div>

<section class="abs welcome">
  <div class="photo"><div role="img" aria-label="Diner with a glass of red wine at a plated meal"></div></div>
  <h2>Welcome To <b>Bright Plate &amp; Vine Fair</b></h2>
  <p><b>Lorem Ipsum is simply dummy text of the printing and typesetting industry. Lorem Ipsum has been the indus-try's standard dummy text ever since the 1500s,</b> when an unknown printer took a galley of type and scrambled it to make a type specimen book. It has survived not only five centuries, but also the leap into five centuries, but also the leap inelectronic typesetting, remaining essentially unchanged.</p>
</section>

<div class="abs about-icon" role="img" aria-label="Wine bottle and glasses"></div>
<div class="abs about-h">What is the <em>Bright Plate &amp; Vine Fair?</em></div>
<div class="abs about-rule"></div>
<div class="abs about">
  <p><b>What a year for good food and wine!</b><br>Melbourne, Sydney, Perth, Adelaide and Brisbane have all had the chance to experience the fun, excitement and joy, that is the Bright Plate &amp; Vine Fair!</p>
  <p>We would like to thank all our amazing visitors for coming along and helping us celebrate another awesome year - A big thank you also to the rest of the crew including exhibitors, sponsors and chefs!</p>
  <p>Make sure you visit the website early next year for all the details of the 2012 Shows - or sign up to our newsletter to be the first to find out when we are on sale and to receive special discounts and offers!</p>
</div>
<div class="abs more">Moreinfo</div>
<div class="abs shadow" style="left:72px;top:884px;width:570px"></div>

<div class="abs tab exhibit">Want to Exhibit?</div>
<div class="abs tab volunteer">Volunteer for the show</div>
<form class="abs signup">
  <h3>Sign up</h3>
  <label style="left:11px;top:50px">User Name :</label><span class="field" style="top:44px"></span>
  <label style="left:20px;top:73px">Password :</label><span class="field" style="top:67px"></span>
  <span class="check"></span><label style="left:89px;top:99px">Remember Me</label>
  <label style="left:10px;top:122px">Forgot your password?</label>
  <span class="btn">Sign up</span>
</form>

<article class="abs card active" style="left:71px">
  <div class="img" role="img" aria-label="Wine glass beside a plated meal" style="background:linear-gradient(135deg,#6b4a2a,#e9d9c4 45%,#9a3b1c)"></div>
  <h4>WHO’S EXHIBITING</h4><hr>
  <p><b>Lorem ipsum dolor sit amet, con-sectetuer</b> adipiscing elit. Donec libero. Suspendisse bibendum. Cras id urna.</p>
  <span class="plus"><svg width="18" height="18"><path d="M9 1v16M1 9h16" stroke="#8cba0c" stroke-width="4"/></svg></span>
</article>
<article class="abs card" style="left:269px">
  <div class="img" role="img" aria-label="Wine glass beside a plated meal" style="background:linear-gradient(135deg,#6b4a2a,#e9d9c4 45%,#9a3b1c)"></div>
  <h4>CITY <b>HUB</b></h4><hr>
  <p><b>Lorem ipsum dolor sit amet, con-sectetuer</b> adipiscing elit. Donec libero. Suspendisse bibendum. Cras id urna.</p>
  <span class="plus"><svg width="18" height="18"><path d="M9 1v16M1 9h16" stroke="#8cba0c" stroke-width="4"/></svg></span>
</article>
<article class="abs card" style="left:466px">
  <div class="img" role="img" aria-label="Wine, grapes and cheese on a table" style="background:linear-gradient(135deg,#3a1a12,#7a2a1c 40%,#d8c89a 75%,#8aa84a)"></div>
  <h4><b>PLAN</b> YOUR DAY</h4><hr>
  <p><b>Lorem ipsum dolor sit amet, con-sectetuer</b> adipiscing elit. Donec libero. Suspendisse bibendum. Cras id urna.</p>
  <span class="plus"><svg width="18" height="18"><path d="M9 1v16M1 9h16" stroke="#8cba0c" stroke-width="4"/></svg></span>
</article>

<aside class="abs newex">
  <svg class="abs" style="left:4px;top:6px" width="26" height="24" viewBox="0 0 26 24"><ellipse cx="13" cy="16" rx="11" ry="6" fill="#8a4a2a"/><path d="M6 10L22 2" stroke="#555" stroke-width="2"/></svg>
  <h4>New <b>Exhibitors</b></h4>
  <div class="item" style="top:36px"><i class="thumb" role="img" aria-label="Plated dish"></i><b>Veal Roll</b><span>Melbourne, Sydney, Perth,<br>Adelaide and</span></div>
  <div class="item" style="top:94px"><i class="thumb" role="img" aria-label="Plated dish"></i><b>Veal Roll</b><span>Melbourne, Sydney, Perth,<br>Adelaide and</span></div>
  <div class="item" style="top:152px;border:0"><i class="thumb" role="img" aria-label="Plated dish"></i><b>Veal Roll</b><span>Melbourne, Sydney, Perth,<br>Adelaide and</span></div>
</aside>

<div class="abs pay"><span>PayNest</span><span>Vexa</span><span>MeritCard</span></div>
<div class="abs footer" style="top:1166px"><span>Specials</span>|<span>Advanced Search</span>|<span>Reviews</span>|<span>Create an Account</span>|<span style="padding-right:0">Log In</span></div>
<div class="abs footer" style="top:1181px">Copyright © 2012 Bright Plate &amp; Vine Store<span>Privacy Notice</span>|<span style="padding-right:0">Conditions of Use</span></div>
</body>
</html>
```